Brightwell Holdings -Business Card Design Project

I have a new logo to put onto business cards - attached
The word doc shows how I want it all laid out - front page and rear
The lettering I want is clean and rounded - modern
Updates
Project Deadline Extended
Reason: There was no original deadline!
Target Market(s)
25-49 year old leaders and entrepreneurs in Australia
Industry/Entity Type
Business

```html
<!DOCTYPE html>
<html lang="en">
<head>
<meta charset="utf-8">
<title>Brightwell Holdings – Business Card</title>
<link rel="stylesheet" href="https://fonts.googleapis.com/css2?family=Open+Sans:wght@400;600;700&display=swap">
<style>
  :root {
    --brand-blue: #1f5aa6;
    --ink: #1a1a1a;
    --pattern-light: #f4f4f5;
    --pattern-mid: #e2e3e5;
    --divider: #c9c9c9;
    --page: #ffffff;
  }
  * { margin: 0; padding: 0; box-sizing: border-box; }
  html, body {
    width: 1200px; height: 456px; overflow: hidden;
    background: var(--page);
    font-family: "Open Sans", Arial, sans-serif;
    color: var(--ink);
  }
  .sheet { position: relative; width: 1200px; height: 456px; }

  /* front of card */
  .card-front {
    position: absolute; left: 40px; top: 67px; width: 512px; height: 317px;
  }
  .front-texture {
    position: absolute; inset: 0;
    background: linear-gradient(135deg, var(--pattern-light) 0%, var(--pattern-mid) 50%, var(--pattern-light) 100%);
  }
  .brand {
    position: absolute; display: flex; align-items: center; gap: 18px;
  }
  .brand-mark {
    width: 92px; height: 92px; background: var(--brand-blue); flex: none;
  }
  .brand-name {
    color: var(--brand-blue); font-weight: 600; letter-spacing: 0.12em;
    text-transform: uppercase; line-height: 1.1;
  }
  .card-front .brand { left: 30px; top: 62px; }
  .card-front .brand-name { font-size: 34px; }

  .front-tagline {
    position: absolute; left: 0; width: 526px; top: 202px;
    text-align: center; font-size: 15px; line-height: 19px;
  }
  .front-person {
    position: absolute; left: 0; width: 526px; top: 246px;
    text-align: center; font-size: 19px; font-weight: 700; letter-spacing: 0.02em;
  }

  /* fold divider */
  .divider {
    position: absolute; left: 582px; top: 0; width: 4px; height: 456px;
    border-left: 1px solid var(--divider); border-right: 1px solid var(--divider);
  }

  /* back of card */
  .services {
    position: absolute; left: 588px; top: 171px;
    list-style: none; font-size: 15px; line-height: 21.5px;
  }
  .contact {
    position: absolute; left: 590px; top: 280px;
    font-size: 14.5px; line-height: 23px;
  }
  .card-back .brand {
    left: 944px; top: 214px; flex-direction: column; gap: 10px; width: 224px;
  }
  .card-back .brand-mark { width: 56px; height: 56px; }
  .card-back .brand-name { font-size: 21px; text-align: center; }
  .abn {
    position: absolute; left: 940px; width: 232px; top: 356px;
    text-align: center; font-size: 21px;
  }
</style>
</head>
<body>
<main class="sheet">
  <section class="card-front">
    <div class="front-texture" role="img" aria-label="Light grey geometric tiled background texture"></div>
    <div class="brand">
      <span class="brand-mark" aria-hidden="true"></span>
      <span class="brand-name">Brightwell<br>Holdings</span>
    </div>
    <p class="front-tagline">Direction and Growth<br>For Leaders and Entrepreneurs</p>
    <p class="front-person">Owen Hartley - Director</p>
  </section>

  <div class="divider" aria-hidden="true"></div>

  <section class="card-back">
    <ul class="services">
      <li>NLP Practitioner &amp; Coach</li>
      <li>Personal, Business &amp; Staff Development</li>
      <li>Self Resilience Programs</li>
    </ul>
    <address class="contact" style="font-style:normal">
      Phone: 0400 218 764<br>
      Email: owen@brightwellholdings.com.au<br>
      Web:&nbsp; brightwellholdings.com.au
    </address>
    <div class="brand">
      <span class="brand-mark" aria-hidden="true"></span>
      <span class="brand-name">Brightwell<br>Holdings</span>
    </div>
    <p class="abn">ABN: 42 617 309 258</p>
  </section>
</main>
</body>
</html>
```